Seasons Greetings from Brackfold Hire.

Brackfold Hire is a Temporary Structures company based in South East London (South Bermondsey).
We dry hire Brackfold as well as deliver and manage projects with our own crew.
We are looking for someone to design our Christmas card or as I prefer to say ‘Season’s Greetings Card’ as this includes everyone religious or not.
The card should reflect Brackfold Hire Ltd and what we do, if you take a look at our website please look at the hires section only,
http://www.brackfold.co.uk/stage-hire.htm
Also take a look at our Brackfold Video’s
http://www.vidplume.example/user/firstbrackfold?feature=results_main
We would also like the card to be friendly and humorous,
Card Size: 210mm x 297mm folded to 210mm x 148mm
Suggested text for Front of card: Seasons Greetings from Brackfold Hire
Inner Text has yet to be confirmed but something like: Wishing you a Merry Christmas and a Happy New Year from everyone at Brackfold Hire
A clever use of the Brackfold logo or weave of the deck would be proffered. I have attached a PDF of a previous card.
Please DO Not show the Mantis Risers.
Please let me know if you require anymore info,
Target Market(s)
Brackfold Customers
Industry/Entity Type
Religious
Requirements
Must have
- Must be a professional looking card

```html
<!DOCTYPE html>
<html lang="en">
<head>
<meta charset="utf-8">
<title>Season's Greetings Card – Brackfold Hire</title>
<link rel="stylesheet" href="https://fonts.googleapis.com/css2?family=Nothing+You+Could+Do&family=Pinyon+Script&family=Oswald:wght@600&display=swap">
<style>
  :root {
    --page: #ffffff;
    --label: #333333;
    --silver-light: #f4f4f6;
    --silver-mid: #d9d9de;
    --silver-dark: #a9a8b0;
    --silver-band: #8f8e97;
    --fold-shade: rgba(0, 0, 0, 0.07);
    --flake-blue: rgba(46, 98, 178, 0.55);
    --flake-blue-soft: rgba(46, 98, 178, 0);
    --flake-white: rgba(255, 255, 255, 0.85);
    --flake-white-soft: rgba(255, 255, 255, 0);
    --navy: #1f2a68;
    --script-ink: #4a4a55;
    --greeting-ink: #ffffff;
    --shadow: rgba(0, 0, 0, 0.35);
  }

  html, body {
    margin: 0;
    padding: 0;
    width: 1200px;
    height: 900px;
    overflow: hidden;
    background: var(--page);
  }

  .canvas {
    position: relative;
    width: 1200px;
    height: 900px;
  }

  .view-label {
    position: absolute;
    margin: 0;
    font-family: Arial, Helvetica, sans-serif;
    font-size: 13px;
    letter-spacing: 0.4px;
    color: var(--label);
  }
  .view-label--front  { left: 682px;  top: 30px; }
  .view-label--back   { left: 66px;   top: 576px; }
  .view-label--inside { left: 1006px; top: 864px; }

  .spread {
    position: absolute;
    display: flex;
    box-shadow: 4px 6px 10px var(--shadow);
  }

  .panel {
    position: relative;
    height: 100%;
  }

  /* Outer spread: back + front */
  .spread--outer {
    left: 66px;
    top: 54px;
    width: 744px;
    height: 508px;
    z-index: 2;
  }
  .spread--outer .panel--back  { width: 370px; }
  .spread--outer .panel--front { width: 374px; }

  .snowfall {
    position: absolute;
    inset: 0;
  }

  .panel--back .snowfall {
    background:
      radial-gradient(circle at 60px 370px, var(--flake-white) 0, var(--flake-white-soft) 26px),
      radial-gradient(circle at 300px 420px, var(--flake-white) 0, var(--flake-white-soft) 24px),
      radial-gradient(circle at 130px 460px, var(--flake-white) 0, var(--flake-white-soft) 18px),
      radial-gradient(circle at 250px 330px, var(--flake-white) 0, var(--flake-white-soft) 20px),
      radial-gradient(circle at 70px 30px, var(--flake-white) 0, var(--flake-white-soft) 22px),
      radial-gradient(circle at 200px 60px, var(--flake-white) 0, var(--flake-white-soft) 20px),
      radial-gradient(ellipse 260px 120px at 180px 300px, rgba(255,255,255,0.45), rgba(255,255,255,0)),
      linear-gradient(180deg,
        var(--silver-light) 0%,
        var(--silver-mid) 35%,
        var(--silver-band) 60%,
        var(--silver-mid) 78%,
        var(--silver-light) 100%);
  }

  .panel--front .snowfall {
    background:
      radial-gradient(circle at 116px 86px, var(--flake-white) 0, var(--flake-blue) 14px, var(--flake-blue-soft) 36px),
      radial-gradient(circle at 238px 262px, var(--flake-white) 0, var(--flake-blue) 26px, var(--flake-blue-soft) 72px),
      radial-gradient(circle at 88px 414px, var(--flake-white) 0, var(--flake-blue) 14px, var(--flake-blue-soft) 40px),
      radial-gradient(circle at 334px 106px, var(--flake-white) 0, var(--flake-blue) 8px, var(--flake-blue-soft) 22px),
      radial-gradient(circle at 312px 466px, var(--flake-white) 0, var(--flake-blue) 8px, var(--flake-blue-soft) 20px),
      radial-gradient(circle at 38px 256px, var(--flake-white) 0, var(--flake-white-soft) 20px),
      radial-gradient(circle at 200px 50px, var(--flake-white) 0, var(--flake-white-soft) 22px),
      radial-gradient(circle at 340px 440px, var(--flake-white) 0, var(--flake-white-soft) 24px),
      radial-gradient(circle at 30px 380px, var(--flake-white) 0, var(--flake-white-soft) 18px),
      radial-gradient(circle at 150px 470px, var(--flake-white) 0, var(--flake-white-soft) 18px),
      linear-gradient(180deg,
        var(--silver-light) 0%,
        var(--silver-mid) 35%,
        var(--silver-band) 60%,
        var(--silver-mid) 78%,
        var(--silver-light) 100%);
  }

  .panel--front::before {
    content: "";
    position: absolute;
    left: 0; top: 0; bottom: 0;
    width: 3px;
    background: var(--fold-shade);
    z-index: 1;
  }

  .back-brand {
    position: absolute;
    left: 144px;
    top: 402px;
    margin: 0;
    font-family: "Oswald", sans-serif;
    font-weight: 600;
    font-size: 16px;
    line-height: 1;
    letter-spacing: 0.5px;
    text-transform: uppercase;
    color: var(--greeting-ink);
  }

  /* Inside spread */
  .spread--inside {
    left: 396px;
    top: 340px;
    width: 744px;
    height: 500px;
    z-index: 1;
  }
  .spread--inside .panel--left  { width: 364px; }
  .spread--inside .panel--right { width: 380px; }

  .panel--left {
    background: linear-gradient(180deg,
      var(--silver-light) 0%,
      var(--silver-mid) 30%,
      var(--silver-dark) 55%,
      var(--silver-mid) 75%,
      var(--silver-light) 100%);
  }
  .panel--right {
    background: linear-gradient(180deg,
      #fafafb 0%,
      var(--silver-light) 35%,
      var(--silver-band) 60%,
      var(--silver-mid) 80%,
      #fafafb 100%);
  }

  .inside-wish {
    position: absolute;
    left: 100px;
    top: 160px;
    margin: 0;
    font-family: "Nothing You Could Do", cursive;
    font-size: 18px;
    color: var(--script-ink);
    white-space: nowrap;
    transform: rotate(-2deg);
  }

  .inside-greeting {
    position: absolute;
    left: 102px;
    top: 238px;
    margin: 0;
    font-family: "Pinyon Script", cursive;
    font-weight: 400;
    font-size: 26px;
    color: var(--greeting-ink);
    white-space: nowrap;
  }

  .inside-brand {
    position: absolute;
    left: 102px;
    top: 312px;
    display: flex;
    align-items: center;
    gap: 10px;
  }
  .inside-brand__mark {
    width: 20px;
    height: 20px;
    background: var(--navy);
  }
  .inside-brand__name {
    margin: 0;
    font-family: "Oswald", sans-serif;
    font-weight: 600;
    font-size: 40px;
    line-height: 1;
    text-transform: uppercase;
    color: var(--navy);
    letter-spacing: 1px;
  }
</style>
</head>
<body>
<main class="canvas">
  <p class="view-label view-label--front">(FRONT OF CARD)</p>

  <section class="spread spread--outer" aria-label="Outside of card">
    <div class="panel panel--back">
      <div class="snowfall" role="img" aria-label="Soft falling white snowflakes over a brushed silver background"></div>
      <p class="back-brand">Brackfold</p>
    </div>
    <div class="panel panel--front">
      <div class="snowfall" role="img" aria-label="Large blue and silver crystal snowflakes scattered among small white snowflakes on brushed silver"></div>
    </div>
  </section>

  <p class="view-label view-label--back">(BACK OF CARD)</p>

  <section class="spread spread--inside" aria-label="Inside of card">
    <div class="panel panel--left"></div>
    <div class="panel panel--right">
      <p class="inside-wish">wishing all the best for 2013</p>
      <h1 class="inside-greeting">Season's Greetings</h1>
      <div class="inside-brand">
        <span class="inside-brand__mark"></span>
        <p class="inside-brand__name">Brackfold</p>
      </div>
    </div>
  </section>

  <p class="view-label view-label--inside">(INSIDE OF CARD)</p>
</main>
</body>
</html>
```